Creative, Modern Annual Report for Non-profit, Famnest

We need a clean and creative annual report for a non-profit helping older kids find families. We are including a word document, some information is not complete, please see notes. The document has names of photos and thumbnails to help point you in the right direction. Please see filecrate file for everything you need. Thank you! https://www.filecrate-share.net/sh/qx7tm2lwk3vrp8a/ZZKpL4mwTQEbvNa7ZRfhydkPLuWq?dl=0

Font styles to use
Sans Serif

Requirements
Must have
• Choose from these Branding Colors
• #Fex525
• #ff5000
• #00000
• #057688
• #5ab3c2

```html
<!DOCTYPE html>
<html lang="en">
<head>
<meta charset="utf-8">
<title>Famnest Annual Report – Page 6</title>
<link rel="stylesheet" href="https://fonts.googleapis.com/css2?family=Arimo:wght@400;700&display=swap">
<style>
  :root {
    --gold: #fec525;
    --ink: #111111;
    --paper: #ffffff;
  }
  html, body {
    margin: 0;
    padding: 0;
    overflow: hidden;
    background: var(--paper);
  }
  .page {
    position: relative;
    width: 927px;
    height: 1200px;
    overflow: hidden;
    background: var(--paper);
    font-family: "Arimo", Arial, sans-serif;
    color: var(--ink);
  }
  .rule {
    position: absolute;
    left: 55px;
    width: 817px;
    height: 5px;
    border-top: 1.5px solid var(--gold);
    border-bottom: 1.5px solid var(--gold);
    box-sizing: border-box;
  }
  .rule--top { top: 78px; }
  .rule--bottom { top: 1122px; }
  .brand-mark {
    position: absolute;
    left: 438px;
    top: 55px;
    width: 50px;
    height: 50px;
    border: 2px solid var(--gold);
    border-radius: 50%;
    background: var(--paper);
    box-sizing: border-box;
    display: flex;
    align-items: center;
    justify-content: center;
    font-size: 9px;
    font-weight: 700;
    color: var(--ink);
  }
  .page-number {
    position: absolute;
    left: 447px;
    top: 1108px;
    width: 32px;
    height: 32px;
    border: 1.5px solid var(--gold);
    border-radius: 50%;
    background: var(--paper);
    box-sizing: border-box;
    display: flex;
    align-items: center;
    justify-content: center;
    font-size: 15px;
    color: var(--gold);
  }
  .section-title {
    position: absolute;
    left: 0;
    width: 927px;
    margin: 0;
    text-align: center;
    font-size: 19.5px;
    font-weight: 700;
  }
  .section-title--kids { top: 113px; }
  .section-title--results { top: 297px; }
  .copy {
    position: absolute;
    left: 81px;
    width: 762px;
    margin: 0;
    font-size: 16px;
    line-height: 25.6px;
  }
  .copy .line { display: block; }
  .copy .line--full { text-align: justify; text-align-last: justify; }
  .copy .line--indent { padding-left: 28px; }
  .copy--kids { top: 139px; }
  .copy--gallery { top: 215px; }
  .copy--results { top: 323px; }
</style>
</head>
<body>
<div class="page">
  <div class="rule rule--top"></div>
  <div class="brand-mark">Famnest</div>

  <h2 class="section-title section-title--kids">Who are the Kids?</h2>
  <p class="copy copy--kids">
    <span class="line line--full line--indent">___% of the children who come to Weekend Bridges LA are _____ or older and have been in</span>
    <span class="line">foster care for an average of ____ years.</span>
  </p>
  <p class="copy copy--gallery">
    <span class="line line--full line--indent">Children currently in need of families in Los Angeles can be viewed on Famnest’s website www.</span>
    <span class="line">famnest.org under “Galleries”.</span>
  </p>

  <h2 class="section-title section-title--results">Results</h2>
  <p class="copy copy--results">
    <span class="line line--full line--indent">As of the end of 2018 Weekend Bridges LA served_____ youth, ____ youth participated, ____</span>
    <span class="line line--full">were hosted and ____ found Permanency (___ matched for adoption ___ matched for guardianship).</span>
    <span class="line">_____ Weekend Bridges kids had finalized adoptions and guardianships in 2019.</span>
  </p>

  <div class="rule rule--bottom"></div>
  <div class="page-number">6</div>
</div>
</body>
</html>
```